Veltrane CRM Sales Brochure

We need a sales brochure to be designed to help us promote our Orbalux C.R.M. (Customer Relationship Management) products and services. Designs aren't limited to just one side. We'd like to see professional, yet creative and fun design concepts incorporating the logo branding. Our target market will be both "White Collar" industry (Accountants / Solicitors / Business Insurance Agencies) as well as "Blue Collar" Industry (Manufacturing / Construction / Electricians). The final design should communicate our business as an experienced provider of Orbalux C.R.M. solutions. Attached files include Logo and Draft Content

```html
<!DOCTYPE html>
<html lang="en">
<head>
<meta charset="utf-8">
<title>Veltrane CRM Sales Brochure</title>
<link href="https://fonts.googleapis.com/css2?family=Open+Sans:wght@400;600;700;800&display=swap" rel="stylesheet">
<style>
:root{
  --page:#f3f3f3;
  --ink:#3a3a3a;
  --ink-soft:#4a4a4a;
  --sky:#45c3f0;
  --sky-deep:#1b8fc4;
  --navy:#0b3a63;
  --orange:#f0a020;
  --orange-ring:#fbe3b3;
  --footer:#3b3b3d;
  --slate-top:#3d3d3f;
  --slate-bottom:#8a8a8c;
  --white:#ffffff;
  --stage:#e4e4e4;
}
*{box-sizing:border-box;margin:0;padding:0}
html,body{width:1200px;height:861px;overflow:hidden}
body{background:var(--stage);font-family:"Open Sans",sans-serif;color:var(--ink);position:relative}
.page{position:absolute;top:35px;width:560px;height:792px;background:var(--page);overflow:hidden;box-shadow:0 2px 8px rgba(0,0,0,.18)}
.page--front{left:30px}
.page--back{left:610px}

.hero{position:absolute;top:12px;height:341px;background:radial-gradient(circle at 75% 35%,#7fd6f5 0%,#1d8ec4 35%,#0b4f84 70%,#062a4b 100%)}
.page--front .hero{left:20px;width:518px;border-radius:0 42px 0 42px}
.page--back .hero{left:22px;width:520px;border-radius:0 36px 0 36px;background:linear-gradient(135deg,#0d4d7f 0%,#2aa0d6 45%,#d7f1fb 62%,#1f79ad 80%,#08375f 100%)}
.hero__word{position:absolute;right:40px;top:130px;font-size:52px;font-weight:800;color:var(--white);letter-spacing:-1px;opacity:.95}

.logo-card{position:absolute;z-index:3;top:0;width:160px;height:125px;background:var(--white);border-radius:0 0 10px 10px;display:flex;flex-direction:column;align-items:center;justify-content:center;gap:10px}
.page--front .logo-card{left:32px}
.page--back .logo-card{left:35px}
.logo-card__mark{width:34px;height:34px;background:var(--sky)}
.logo-card__name{font-size:26px;font-weight:600;color:#4a4a4a;letter-spacing:2px}

.badge{position:absolute;z-index:3;border-radius:50%;background:var(--orange);border:4px solid var(--orange-ring);box-shadow:0 0 0 2px var(--orange);display:flex;flex-direction:column;align-items:center;justify-content:center;color:var(--white);font-weight:700;line-height:1.2;text-align:center}
.page--front .badge{left:412px;top:254px;width:128px;height:128px;font-size:20px}
.page--back .badge{left:445px;top:264px;width:104px;height:104px;font-size:17px}

.headline{position:absolute;left:20px;top:378px;width:260px;font-size:16.5px;font-weight:700;line-height:1.35;color:var(--ink)}
.headline em{font-style:normal;color:var(--sky)}
.body-col{position:absolute;left:20px;top:456px;width:252px}
.body-col p{font-size:8.4px;line-height:1.45;text-align:justify;margin-bottom:9px;color:var(--ink-soft)}

.blue-col{position:absolute;z-index:1;left:282px;top:334px;width:278px;height:458px;background:var(--sky);border-radius:40px 0 0 0}
.pitch{position:absolute;left:14px;width:254px;color:#0e2a3d;font-size:8.4px;line-height:1.45;text-align:justify}
.pitch__icon{float:left;width:34px;height:30px;margin:2px 6px 0 0}
.pitch--1{top:62px}
.pitch--2{top:190px}
.pitch--3{top:327px}
.rule{position:absolute;left:0;width:278px;height:1px;background:rgba(255,255,255,.55)}

.footer{position:absolute;z-index:2;left:0;bottom:24px;width:560px;height:24px;background:var(--footer);display:flex;justify-content:space-between;align-items:center;padding:0 32px 0 16px;color:var(--white);font-size:10px;font-weight:700;letter-spacing:.5px}
.footer span{display:flex;align-items:center;gap:5px}
.footer svg{width:10px;height:10px}
.page--front .footer-strip{position:absolute;z-index:1;left:282px;bottom:0;width:278px;height:24px;background:var(--sky)}

.intro{position:absolute;left:22px;top:370px;width:518px;font-size:8.5px;line-height:1.45;text-align:justify;color:var(--ink-soft)}

.tab{position:absolute;left:0;width:303px;background:var(--sky);border-radius:0 26px 26px 0;padding:9px 80px 0 22px;color:#0e2a3d}
.tab h3{font-size:10px;font-weight:700;margin-bottom:3px}
.tab h3 em{font-style:normal;font-weight:600;color:var(--white)}
.tab p{font-size:7.6px;line-height:1.45;text-align:justify}
.tab__icon{position:absolute;right:14px;top:50%;transform:translateY(-50%);width:50px;height:50px}
.tab__divider{position:absolute;right:72px;top:14%;height:72%;width:1px;background:rgba(255,255,255,.7)}
.tab--marketing{top:453px;height:87px}
.tab--sales{top:546px;height:87px}
.tab--service{top:647px;height:86px}

.package{position:absolute;left:319px;top:453px;width:241px;height:280px;background:linear-gradient(180deg,var(--slate-top),var(--slate-bottom));border-radius:8px 0 0 8px;padding:14px 14px 0 17px;color:var(--white)}
.package__title{font-size:10px;line-height:1.3;margin-bottom:12px}
.package__grid{display:grid;grid-template-columns:1fr 1fr;row-gap:5px;margin-bottom:18px}
.package__note{font-size:9.4px;line-height:1.3;text-align:justify;margin-bottom:6px}
.ticks{list-style:none}
.ticks li,.package__grid span{font-size:8.7px;display:flex;align-items:center;gap:7px;line-height:1.7}
.ticks li::before,.package__grid span::before{content:"";width:7px;height:7px;border-radius:50%;background:var(--sky);flex:none}
</style>
</head>
<body>

<section class="page page--front">
  <div class="hero" role="img" aria-label="Hand touching a glowing CRM interface with globe, contact card, chart and people icons on blue"><span class="hero__word">CRM</span></div>
  <div class="logo-card"><span class="logo-card__mark"></span><span class="logo-card__name">VELTRANE</span></div>

  <h1 class="headline">ENHANCE YOUR CUSTOMER EXPERIENCES TO <em>GROW</em><br>YOUR BUSINESS FASTER</h1>
  <div class="body-col">
    <p>Leveraging existing customer value via a tailored Customer Relationship Management (CRM) system is far more cost effective than prospecting for new customers. In simple terms, CRM is a technological strategy focused on managing ongoing relationships with your customers to ensure they are provided with the information they seek to enable them to purchase at the time they choose.</p>
    <p>In a digitally connected world, customer purchase perceptions are forming pre, during and post their interaction with your brand. Customers are seeking to be satisfied with the quality of your products and services, but a complicated sales process or poor service engagement will worsen overall impressions typically resulting in the like lihood of no sales transactions.</p>
    <p>CRM is the art/act of developing a working relationship with your customers, where they feel a sense of individual importance. CRM solutions increase your profitability by streamlining administrative processes in your sales, marketing, and service divisions, and letting you focus on building and maintaining the customer relationships that matter. A strong CRM solution is a multifaceted platform where everything crucial to developing, improving, and retaining your customer relationships is stored.</p>
  </div>

  <div class="blue-col">
    <p class="pitch pitch--1"><svg class="pitch__icon" viewBox="0 0 34 30"><rect x="1" y="16" width="4" height="13" fill="#fff"/><rect x="7" y="11" width="4" height="18" fill="#fff"/><path d="M22 4a10 10 0 1 0 10 10H22z" fill="#fff"/><path d="M24 2a10 10 0 0 1 10 10H24z" fill="#fff"/></svg>Without the support of an integrated CRM solution, you may miss growth opportunities and lose revenue because you're not optimizing your operating processes or making the most of your customer relationships or sales leads.</p>
    <div class="rule" style="top:154px"></div>
    <p class="pitch pitch--2"><svg class="pitch__icon" viewBox="0 0 34 30"><circle cx="17" cy="8" r="7" fill="#fff"/><path d="M3 30c0-9 6-13 14-13s14 4 14 13z" fill="#fff"/></svg>Imagine misplacing customer contact information, only to learn that your delay resulted in losing your client to a competitor. Or, picture your top two salespeople pursuing the same prospect, resulting in an annoyed potential customer and some unfriendly, in-house competition. Without a centralized and automated CRM system, your people can lose track of customer interactions and miss business opportunities.</p>
    <div class="rule" style="top:300px"></div>
    <p class="pitch pitch--3"><svg class="pitch__icon" viewBox="0 0 34 30"><rect x="2" y="20" width="5" height="10" fill="#fff"/><rect x="10" y="15" width="5" height="15" fill="#fff"/><rect x="18" y="11" width="5" height="19" fill="#fff"/><rect x="26" y="7" width="5" height="23" fill="#fff"/><path d="M2 14 12 7l6 4L31 1" stroke="#fff" stroke-width="2.5" fill="none"/></svg>If you want a competitive advantage in your marketplace, a tailored CRM solution is the simple answer. CRM can take the burden of managing your customers. It enables automation of your customer management processes so you can focus on what's important: leading your business to succeed.</p>
  </div>

  <div class="badge"><span>SIMPLER</span><span>SYSTEMS</span></div>

  <div class="footer-strip"></div>
  <footer class="footer">
    <span><svg viewBox="0 0 10 10"><circle cx="5" cy="5" r="5" fill="var(--sky)"/></svg>support@veltrane.com</span>
    <span><svg viewBox="0 0 10 10"><circle cx="5" cy="5" r="4" fill="none" stroke="var(--sky)" stroke-width="1.6"/><path d="M3.5 3.5 5 5.5 6.5 4" stroke="var(--sky)" fill="none"/></svg>(07) 5550 0142</span>
    <span><svg viewBox="0 0 10 10"><circle cx="5" cy="5" r="4" fill="none" stroke="var(--sky)" stroke-width="1.6"/><circle cx="5" cy="5" r="1.6" fill="var(--sky)"/></svg>www.veltrane.com</span>
  </footer>
</section>

<section class="page page--back">
  <div class="hero" role="img" aria-label="Businessman in a suit studying a large blue wall of glowing line and bar charts"></div>
  <div class="logo-card"><span class="logo-card__mark"></span><span class="logo-card__name">VELTRANE</span></div>
  <div class="badge"><span>SIMPLER</span><span>SYSTEMS</span></div>

  <p class="intro">Veltrane are experts in tailored CRM systems to suit businesses and departments of all sizes across a wide range of Government, Commercial and Not-for-Profit industry sectors. Using the power of Orbalux Relay 365 we are able to install and configure a flexible solution that's customizable to suit your specific requirements. You have the choice of a stand-alone application to meet the needs of a specific line of business or use multiple CRM tools that work together as a powerful integrated solution across marketing, sales and customer service.</p>

  <div class="tab tab--marketing">
    <h3>MARKETING: <em>ENHANCE &amp; NURTURE</em></h3>
    <p>Generate multichannel marketing campaigns, foster sales-ready leads, and align your sales and marketing teams with planning and tracking tools that integrate with your existing apps and services.</p>
    <span class="tab__divider"></span>
    <svg class="tab__icon" viewBox="0 0 50 50"><rect x="6" y="10" width="28" height="20" rx="2" fill="none" stroke="#fff" stroke-width="2"/><rect x="16" y="30" width="8" height="6" fill="#fff"/><rect x="12" y="36" width="16" height="2" fill="#fff"/><rect x="10" y="14" width="10" height="3" fill="#fff"/><rect x="10" y="20" width="18" height="2" fill="#fff"/><path d="M38 14h8M38 22h8M38 30h8" stroke="#fff" stroke-width="2"/></svg>
  </div>
  <div class="tab tab--sales">
    <h3>SALES: <em>ENGAGE &amp; CONNECT</em></h3>
    <p>Go beyond sales automation to better understand customer needs, engage more effectively, and win more deals. Sell smarter with embedded insights, foster relationships, boost productivity and accelerate sales performance.</p>
    <span class="tab__divider"></span>
    <svg class="tab__icon" viewBox="0 0 50 50"><circle cx="25" cy="25" r="11" fill="none" stroke="#fff" stroke-width="2"/><text x="25" y="30" text-anchor="middle" font-family="Open Sans,sans-serif" font-size="14" font-weight="700" fill="#fff">$</text><g stroke="#fff" stroke-width="1.5"><path d="M25 14V5M25 36v9M14 25H5M36 25h9M17 17l-6-6M33 33l6 6M33 17l6-6M17 33l-6 6"/></g><g fill="#fff"><circle cx="25" cy="4" r="3"/><circle cx="25" cy="46" r="3"/><circle cx="4" cy="25" r="3"/><circle cx="46" cy="25" r="3"/><circle cx="10" cy="10" r="3"/><circle cx="40" cy="40" r="3"/><circle cx="40" cy="10" r="3"/><circle cx="10" cy="40" r="3"/></g></svg>
  </div>
  <div class="tab tab--service">
    <h3>CUSTOMER SERVICE: <em>FOSTER &amp; SUPPORT</em></h3>
    <p>Deliver guided, intelligent service and support on any channel with a unique ability to work with your existing systems. Empower customers and agents with the tools they need to ensure quick and accurate resolution, every time.</p>
    <span class="tab__divider"></span>
    <svg class="tab__icon" viewBox="0 0 50 50"><circle cx="25" cy="20" r="9" fill="#fff"/><path d="M14 20a11 11 0 0 1 22 0" fill="none" stroke="#fff" stroke-width="2.5"/><rect x="11" y="18" width="5" height="8" rx="2" fill="#fff"/><rect x="34" y="18" width="5" height="8" rx="2" fill="#fff"/><path d="M36 26q0 6-8 7" fill="none" stroke="#fff" stroke-width="1.5"/><path d="M9 46c0-9 7-13 16-13s16 4 16 13z" fill="#fff"/></svg>
  </div>

  <aside class="package">
    <p class="package__title">Foundation CRM solution $4,990 + GST<br>Inclusions;</p>
    <div class="package__grid">
      <span>Briefing</span><span>Configuration</span>
      <span>Setup</span><span>Live launch</span>
      <span>Installation</span><span>Training</span>
    </div>
    <p class="package__note">To further enhance the power of your Orbalux CRM solution we offer broader modules and services that include;</p>
    <ul class="ticks">
      <li>Ongoing personalised support</li>
      <li>Customised coding and development</li>
      <li>Bespoke modules</li>
      <li>Broader integration across wider systems</li>
      <li>Customised reporting</li>
      <li>Data migration</li>
    </ul>
  </aside>

  <footer class="footer">
    <span><svg viewBox="0 0 10 10"><circle cx="5" cy="5" r="5" fill="var(--sky)"/></svg>support@veltrane.com</span>
    <span><svg viewBox="0 0 10 10"><circle cx="5" cy="5" r="4" fill="none" stroke="var(--sky)" stroke-width="1.6"/><path d="M3.5 3.5 5 5.5 6.5 4" stroke="var(--sky)" fill="none"/></svg>(07) 5550 0142</span>
    <span><svg viewBox="0 0 10 10"><circle cx="5" cy="5" r="4" fill="none" stroke="var(--sky)" stroke-width="1.6"/><circle cx="5" cy="5" r="1.6" fill="var(--sky)"/></svg>www.veltrane.com</span>
  </footer>
</section>

</body>
</html>
```